marlow pennant website Redesign

Read the Company mission statement and then help us redesign the website along the guidelines in the design brief and using the logo and fonts supplied.

The current marlow pennant website is very dated but has been very sucessful, we would like to invest in a brand refresh and site rebuild to bring the website up to 2018 standard.

We have using cut and paste from other travel websites made a pdf mock up of what sort of content we need on the pages and the lay out we like.

Target Market(s)

+45 Plus experienced Marlow Pennant, established, educated

Number of Pages Required

4 page

Font styles to use
Sans Serif

Requirements
Must have
• There is a full brief document and mock up, it must follow the brand guidelines
Nice to have
• There is a full brief document and mock up
Should not have
• Looks of a cheap cruise deal travel site

```html
<!DOCTYPE html>
<html lang="en">
<head>
<meta charset="utf-8">
<title>Marlow Pennant</title>
<link rel="stylesheet" href="https://fonts.googleapis.com/css2?family=Montserrat:wght@400;600;700&family=Playfair+Display:wght@400;700&display=swap">
<style>
:root{
  --blue:#1b5fc9;
  --blue-deep:#0f3f96;
  --navy:#0e2c5c;
  --navy-dark:#0a2148;
  --ink:#222629;
  --muted:#5b6166;
  --pale:#edf3e5;
  --grey:#ececec;
  --white:#ffffff;
}
*{box-sizing:border-box;margin:0;padding:0}
html,body{width:1200px;height:4433px;overflow:hidden}
body{font-family:"Montserrat",sans-serif;color:var(--ink);background:var(--white);position:relative}
.serif{font-family:"Playfair Display",serif}
section,header,footer{position:absolute;left:0;width:1200px}
.eyebrow{font-size:15px;font-weight:600;letter-spacing:4px;text-transform:uppercase}
.body-copy{font-size:13px;line-height:19px;color:var(--muted)}
.link{font-size:13px;font-weight:700}

/* header */
.site-header{top:0;height:112px;background:var(--white)}
.topbar{position:absolute;top:0;left:220px;width:790px;height:80px;border-bottom:1px solid #ddd}
.phone{position:absolute;left:0;top:36px;font-size:13px;font-weight:600;display:flex;align-items:center;gap:10px}
.brand{position:absolute;left:50%;transform:translateX(-50%);top:18px;font-size:28px;font-weight:700;color:var(--blue);letter-spacing:1px;white-space:nowrap}
.social{position:absolute;right:0;top:34px;display:flex;gap:22px}
.social span{width:12px;height:12px;border-radius:50%;background:var(--blue)}
.nav{position:absolute;top:86px;left:220px;width:790px;display:flex;justify-content:space-between;font-size:12px;font-weight:700;text-transform:uppercase}

/* hero */
.hero{top:112px;height:544px;background:linear-gradient(180deg,#9ec1dd 0%,#c8dcea 45%,#e6ecef 62%,#7da2bf 78%,#2f5f86 100%)}
.hero-title{position:absolute;top:210px;width:100%;text-align:center;color:var(--white)}
.hero-title .kicker{font-size:22px;font-weight:600;letter-spacing:5px;text-transform:uppercase}
.hero-title .big{font-size:112px;font-weight:700;line-height:110px}
.hero-search{position:absolute;left:296px;top:360px;width:604px;height:44px;background:var(--white);border-radius:4px;padding:0 20px;display:flex;align-items:center;justify-content:space-between;font-size:13px;color:#999}

/* search bar */
.searchbar{top:656px;height:83px;background:var(--blue);color:var(--white)}
.select{position:absolute;top:28px;height:28px;border-bottom:1px solid rgba(255,255,255,.7);font-size:14px;display:flex;justify-content:space-between;align-items:center}
.btn-cruise{position:absolute;left:813px;top:24px;width:158px;height:36px;border-radius:18px;background:var(--white);color:var(--blue);font-size:13px;font-weight:600;display:flex;align-items:center;justify-content:center}
.adv{position:absolute;left:990px;top:34px;font-size:13px;font-weight:700}

/* welcome */
.welcome{top:739px;height:552px}
.welcome-text{position:absolute;left:65px;top:90px;width:590px}
.display{font-size:76px;font-weight:700;line-height:86px;margin:12px 0 24px}
.review{position:absolute;left:798px;top:0;width:402px;height:552px;background:linear-gradient(160deg,var(--blue-deep),var(--blue) 55%,#2c7bd8);color:var(--white);padding:165px 48px 0 48px}
.review q{font-size:31px;font-weight:700;line-height:38px;display:block;quotes:"\201C" "\201D"}

/* two panels */
.feature{top:1291px;height:562px}
.panel{position:absolute;top:0;height:562px}
.panel .txt{position:absolute}
.title-lg{font-size:54px;font-weight:700;line-height:60px}

/* bands */
.band{display:flex;flex-direction:column;align-items:center;justify-content:center;text-align:center}
.band .title-lg{font-size:52px}
.journeys-head{top:1853px;height:168px;background:var(--blue);color:var(--white)}
.tiles{display:flex}
.tile{position:relative;width:300px;height:100%;color:var(--white)}
.tile .t{position:absolute;left:30px;font-size:33px;font-weight:700;line-height:38px}
.journeys{top:2021px;height:322px}
.meta{position:absolute;left:30px;font-size:13px;font-weight:700;display:flex;align-items:center;gap:6px}
.from{position:absolute;left:30px;top:228px;font-size:13px;font-weight:600;line-height:16px}
.from b{font-size:24px;font-weight:400;display:block;margin-top:4px}
.book{position:absolute;left:30px;top:280px;font-size:13px;font-weight:700}
.exp-head{top:2343px;height:169px;background:var(--grey)}
.experiences{top:2512px;height:325px}

/* marketing */
.marketing{top:2837px;height:561px}
.poster{position:absolute;left:798px;top:0;width:402px;height:561px;background:linear-gradient(180deg,#e9eef4 0%,#4b86c7 30%,#7fa9d9 55%,#b9c8a8 75%,#cdbb8c 100%)}
.pager{position:absolute;top:478px;width:92px;height:34px;border-radius:4px;background:var(--blue);color:var(--white);font-size:13px;font-weight:700;display:flex;align-items:center;justify-content:center;gap:8px}

/* region */
.region{top:3398px;height:556px}
.region-copy{position:absolute;left:402px;top:0;width:798px;height:556px;background:var(--pale)}

/* partners */
.partners{top:3954px;height:133px;display:flex;align-items:center;justify-content:space-around;padding:0 80px}
.partners span{font-size:17px;font-weight:700;color:var(--navy)}

/* footer */
.site-footer{top:4087px;height:281px;background:var(--navy);color:var(--white)}
.fcol{position:absolute;top:66px;font-size:12px;line-height:18px}
.fcol h4{font-size:12px;font-weight:700;margin-bottom:6px}
.sub-input{width:170px;height:34px;background:var(--white);display:flex;justify-content:flex-end}
.sub-input span{width:40px;height:34px;background:var(--navy-dark);border:1px solid var(--white);display:flex;align-items:center;justify-content:center}
.fsocial{display:flex;gap:16px;margin-top:8px}
.fsocial span{width:12px;height:12px;border-radius:50%;background:var(--white)}
.copyright{top:4368px;height:65px;background:var(--navy-dark);color:#c7d3e6;font-size:12px;display:flex;align-items:center;justify-content:center}
</style>
</head>
<body>

<header class="site-header">
  <div class="topbar">
    <div class="phone">
      <svg width="14" height="14" viewBox="0 0 24 24"><path fill="#222629" d="M6.6 10.8a15.1 15.1 0 0 0 6.6 6.6l2.2-2.2c.3-.3.7-.4 1-.2 1.1.4 2.3.6 3.6.6.6 0 1 .4 1 1V20c0 .6-.4 1-1 1A17 17 0 0 1 3 4c0-.6.4-1 1-1h3.5c.6 0 1 .4 1 1 0 1.3.2 2.5.6 3.6.1.3 0 .7-.2 1z"/></svg>
      0800 - 55 - 01 - 22
    </div>
    <div class="brand">MARLOW PENNANT</div>
    <div class="social" aria-label="Social links"><span></span><span></span><span></span><span></span><span></span></div>
  </div>
  <nav class="nav">
    <span>Home</span><span>About Us</span><span>Our Cruises</span><span>Destinations</span><span>Exclusive Offers</span><span>Brochures</span><span>Our Team</span><span>Contact</span>
  </nav>
</header>

<section class="hero" role="img" aria-label="Harbour full of moored sailing yachts under a pale blue sky">
  <div class="hero-title">
    <div class="kicker">Travel with</div>
    <div class="big serif">Personality</div>
  </div>
  <div class="hero-search">
    <span>Where do you want to go?</span>
    <svg width="16" height="16" viewBox="0 0 24 24"><circle cx="10" cy="10" r="7" fill="none" stroke="#999" stroke-width="2"/><path d="M15 15l6 6" stroke="#999" stroke-width="2"/></svg>
  </div>
</section>

<section class="searchbar">
  <div class="select" style="left:110px;width:260px"><span>Any Destination</span><span>&#9662;</span></div>
  <div class="select" style="left:385px;width:190px"><span>Sailing Date</span><span>&#9662;</span></div>
  <div class="select" style="left:605px;width:185px"><span>Price Range</span><span>&#9662;</span></div>
  <div class="btn-cruise">Cruise Search</div>
  <div class="adv">Advanced Search</div>
</section>

<section class="welcome">
  <div class="welcome-text">
    <div class="eyebrow">Welcome to</div>
    <h1 class="display serif">Marlow<br>Pennant</h1>
    <p class="body-copy">Lorem ipsum dolor sit amet, consectetur adipiscing elit, sed do eiusmod tempor incididunt ut labore et dolore magna aliqua. Ut enim ad minim veniam, quis nostrud exercitation ullamco laboris nisi ut aliquip ex ea commodo consequat. Duis aute irure dolor in reprehenderit in voluptate velit esse cillum dolore eu fugiat nulla pariatur. Excepteur sint occaecat cupidatat non proident, sunt in culpa qui officia deserunt mollit anim id est laborum. Sed ut perspiciatis unde omnis iste natus error sit voluptatem accusantium doloremque laudantium, totam rem aperiam, eaque ipsa quae ab illo inventore veritatis et quasi architecto.</p>
  </div>
  <div class="review" role="img" aria-label="Aerial view of a cruise ship deck above deep blue sea">
    <q class="serif">Friendly Reliable trusted great to deal with</q>
    <p style="font-size:13px;margin-top:22px">&mdash; Iris Holloway</p>
    <p class="link" style="margin-top:38px">More Reviews &raquo;</p>
  </div>
</section>

<section class="feature">
  <div class="panel" style="left:0;width:402px;background:linear-gradient(180deg,#f4f5f7 0%,#e3e8ee 60%,#cfd8e2 100%)" role="img" aria-label="Polar bear standing on Arctic snow">
    <div class="txt" style="left:58px;top:148px;width:230px">
      <div class="eyebrow" style="font-size:13px">Small Ships</div>
      <h2 class="title-lg serif" style="margin:10px 0 24px">Are<br>the Best</h2>
      <p class="body-copy" style="font-size:12px;line-height:17px">Up close and personal is the way we love our cruise voyages. Whether in the Mediterranean or the Canadian Arctic, small ships enable the discerning cruise traveller to get the best of the world, select from the many destinations.</p>
      <p class="link" style="margin-top:26px">Discover Our Range</p>
    </div>
  </div>
  <div class="panel" style="left:402px;width:798px;background:linear-gradient(120deg,#3a2a22 0%,#6b4a38 40%,#2d2420 100%);color:var(--white)" role="img" aria-label="Smiling chef and crew standing together in a ship dining room">
    <div class="txt" style="left:60px;top:100px;width:330px">
      <div class="eyebrow" style="font-size:13px">You wont find it</div>
      <h2 class="title-lg serif" style="margin:6px 0 18px">Elsewhere</h2>
      <p style="font-size:12px;line-height:17px">Up close and personal is the way we love our cruise voyages. Whether in the Mediterranean or the Canadian Arctic, small ships enable the discerning traveller to get the best of the world, select from the many destinations.</p>
      <p class="link" style="margin-top:18px">Meet the Team</p>
    </div>
  </div>
</section>

<section class="journeys-head band">
  <div class="eyebrow" style="font-size:14px">Featured</div>
  <h2 class="title-lg serif">Journeys</h2>
</section>

<section class="journeys tiles">
  <div class="tile" style="background:linear-gradient(180deg,#4d6d3a,#2f3f2a 60%,#5b4a3a)" role="img" aria-label="River lodge among jungle trees">
    <div class="t serif" style="top:78px">Amazon<br>Cruise</div>
    <div class="meta" style="top:160px"><svg width="12" height="12" viewBox="0 0 24 24"><circle cx="12" cy="12" r="10" fill="#fff"/><path d="M12 6v6l4 2" stroke="#333" stroke-width="2" fill="none"/></svg>4D/3N</div>
    <div class="from">FROM<b>$2,470</b></div><div class="book">Book this &raquo;</div>
  </div>
  <div class="tile" style="background:linear-gradient(180deg,#3a3a3a,#2a2623 60%,#4a3a2c)" role="img" aria-label="Rice bowl dishes on a dark table">
    <div class="t serif" style="top:78px">Buthan Rice<br>Valley Bowls</div>
    <div class="meta" style="top:160px"><svg width="12" height="12" viewBox="0 0 24 24"><circle cx="12" cy="12" r="10" fill="#fff"/><path d="M12 6v6l4 2" stroke="#333" stroke-width="2" fill="none"/></svg>4D/3N</div>
    <div class="from">FROM<b>$2,470</b></div><div class="book">Book this &raquo;</div>
  </div>
  <div class="tile" style="background:linear-gradient(160deg,#2e4a24,#5e8a3a 45%,#1f2a1a)" role="img" aria-label="Fresh green salad in a dark bowl">
    <div class="t serif" style="top:78px">Culinary<br>Vietnam &amp;<br>Cambodia</div>
    <div class="meta" style="top:196px"><svg width="12" height="12" viewBox="0 0 24 24"><circle cx="12" cy="12" r="10" fill="#fff"/><path d="M12 6v6l4 2" stroke="#333" stroke-width="2" fill="none"/></svg>4D/3N</div>
    <div class="book">Book this &raquo;</div>
  </div>
  <div class="tile" style="background:linear-gradient(180deg,#8a9aa3,#5d6b5a 50%,#4a5a40)" role="img" aria-label="Green hills and cliffs over a river">
    <div class="t serif" style="top:78px">Fly around<br>Botswana</div>
    <div class="meta" style="top:160px"><svg width="12" height="12" viewBox="0 0 24 24"><circle cx="12" cy="12" r="10" fill="#fff"/><path d="M12 6v6l4 2" stroke="#333" stroke-width="2" fill="none"/></svg>4D/3N</div>
    <div class="from">FROM<b>$2,470</b></div><div class="book">Book this &raquo;</div>
  </div>
</section>

<section class="exp-head band">
  <div class="eyebrow" style="font-size:14px">Amazing range of</div>
  <h2 class="title-lg serif">Experiences</h2>
</section>

<section class="experiences tiles">
  <div class="tile" style="background:linear-gradient(180deg,#7fa3c0,#3b5d78 55%,#233a4c)" role="img" aria-label="Boat deck on a calm river">
    <div class="t serif" style="top:185px">River<br>Cruise</div><div class="book" style="top:268px">Read more &raquo;</div>
  </div>
  <div class="tile" style="background:linear-gradient(180deg,#a9b9c6,#5d6f7c 55%,#2b3a44)" role="img" aria-label="Steam ship beside snowy mountains">
    <div class="t serif" style="top:185px">Expedition<br>Cruises</div><div class="book" style="top:268px">Book this &raquo;</div>
  </div>
  <div class="tile" style="background:linear-gradient(180deg,#5f7a6a,#3d5a52 50%,#22322c)" role="img" aria-label="Lake with a forested island">
    <div class="t serif" style="top:185px">Fly Free<br>Cruises</div><div class="book" style="top:268px">Book this &raquo;</div>
  </div>
  <div class="tile" style="background:linear-gradient(160deg,#3a2410,#a06a22 50%,#2a1a0c)" role="img" aria-label="Glass of white wine in a warmly lit bar">
    <div class="t serif" style="top:185px">Luxury<br>Cruises</div><div class="book" style="top:268px">Book this &raquo;</div>
  </div>
</section>

<section class="marketing">
  <div class="welcome-text" style="top:118px">
    <div class="eyebrow" style="font-size:14px">Check out our</div>
    <h2 class="title-lg serif" style="font-size:58px;line-height:70px;margin:6px 0 32px">Recent<br>Marketings</h2>
    <p class="body-copy">Lorem ipsum dolor sit amet, consectetur adipiscing elit, sed do eiusmod tempor incididunt ut labore et dolore magna aliqua. Ut enim ad minim veniam, quis nostrud exercitation ullamco laboris nisi ut aliquip ex ea commodo consequat. Duis aute irure dolor in reprehenderit in voluptate velit esse cillum dolore eu fugiat nulla pariatur. Excepteur sint occaecat cupidatat non proident, sunt in culpa qui officia deserunt mollit anim id est laborum. Sed ut perspiciatis unde omnis iste natus error sit voluptatem accusantium doloremque laudantium, totam rem aperiam, eaque ipsa quae ab illo inventore veritatis et quasi architecto.</p>
    <p class="link" style="margin-top:50px">View All</p>
  </div>
  <div class="poster" role="img" aria-label="Brochure advertising a fly free river cruise through Europe">
    <div class="pager" style="left:45px">&lsaquo; Prev</div>
    <div class="pager" style="left:265px">Next &rsaquo;</div>
  </div>
</section>

<section class="region">
  <div style="position:absolute;left:0;top:0;width:402px;height:556px;background:linear-gradient(180deg,#6f8a3e 0%,#a88f5a 45%,#7a6a4a 70%,#c7a35a 100%)" role="img" aria-label="Elephants at a watering hole in the savanna"></div>
  <div class="region-copy">
    <div style="position:absolute;left:65px;top:190px;width:660px">
      <div class="eyebrow" style="font-size:14px">Featured Regions</div>
      <h2 class="title-lg serif" style="font-size:62px;margin:8px 0 20px">Africa</h2>
      <p class="body-copy">Lorem ipsum dolor sit amet, consectetur adipiscing elit, sed do eiusmod tempor incididunt ut labore et dolore magna aliqua. Ut enim ad minim veniam, quis nostrud exercitation ullamco laboris nisi ut aliquip ex ea commodo consequat. Duis aute irure dolor in reprehenderit in voluptate velit esse cillum dolore eu fugiat nulla pariatur. Excepteur sint occaecat cupidatat non proident, sunt in culpa qui officia deserunt mollit anim id est laborum. Nemo enim ipsam voluptatem quia voluptas sit aspernatur aut odit aut fugit, sed quia consequuntur magni dolores eos qui ratione voluptatem sequi nesciunt.</p>
      <div style="display:flex;justify-content:space-between;margin-top:44px" class="link"><span>Prev Region</span><span>Next Region</span></div>
    </div>
  </div>
</section>

<section class="partners" aria-label="Cruise partners">
  <span>Harbourline Cruises</span>
  <span>Azurel Club Voyages</span>
  <span>Paloma Isles</span>
  <span>Sovereign Seas</span>
  <span>Clearwater</span>
</section>

<footer class="site-footer">
  <div class="fcol" style="left:133px;width:230px;top:56px">
    <div style="font-size:20px;font-weight:700;margin-bottom:12px">MARLOW PENNANT</div>
    <p>Lorem ipsum dolor sit amet, consectetur adipiscing elit, sed do eiusmod tempor incididunt ut labore et dolore magna aliqua. Ut enim ad</p>
  </div>
  <div class="fcol" style="left:402px"><h4>Site Map</h4><p>About Us</p><p>Technology</p><p>Partners</p><p>Contact</p></div>
  <div class="fcol" style="left:540px;width:140px"><h4>Quick Links</h4><p>Lorem ipsum dolor sit amet, consectetur adipiscing elit, sed do</p></div>
  <div class="fcol" style="left:710px;width:140px;top:90px"><p>Lorem ipsum dolor sit amet, consectetur adipiscing elit, sed do</p></div>
  <div class="fcol" style="left:916px"><h4>Subscribe</h4>
    <div class="sub-input"><span><svg width="14" height="10" viewBox="0 0 14 10"><rect x=".5" y=".5" width="13" height="9" fill="none" stroke="#fff"/><path d="M.5 .5l6.5 5 6.5-5" fill="none" stroke="#fff"/></svg></span></div>
    <h4 style="margin-top:18px">Follow</h4>
    <div class="fsocial"><span></span><span></span><span></span><span></span><span></span></div>
  </div>
</footer>
<div class="copyright" style="position:absolute;left:0;width:1200px">Website Name, Copyright 2018</div>

</body>
</html>
```